Building company needs a letterhead design

I'm after a modern but professional letter head.
Must have the below details:
- Logo
- Website - TARVELGROUP.COM.AU
- Email - INFO@TARVELGROUP.COM.AU
- Office - 03 58206317
- Mobile number - 0413865290
- ABN - 47 318 264 105
...........................................................................................................................................................................................................................
- Logo
- Office - 03 58206317
- ABN - 47 318 264 105

Target Market(s)

.

Industry/Entity Type

Construction Company

Font styles to use
Sans Serif

Requirements
Must have
• Must have the below details:
• - Logo
• - Website - TARVELGROUP.COM.AU
• - Email - INFO@TARVELGROUP.COM.AU
• - Office - 03 58206317
• - Mobile number - 0413865290
• - ABN - 47 318 264 105
Nice to have
• .
Should not have
• .

```html
<!DOCTYPE html>
<html lang="en">
<head>
<meta charset="utf-8">
<title>Tarvel Building Group – Letterhead</title>
<link rel="stylesheet" href="https://fonts.googleapis.com/css2?family=Arimo:wght@400;700&display=swap">
<style>
  :root {
    --backdrop: #2a2a2b;
    --charcoal: #262627;
    --paper: #f7f7f7;
    --ink: #222222;
    --amber: #f0aa19;
    --amber-light: #f6c54f;
    --grey-mark: #7b7b7d;
    --white: #ffffff;
  }
  * { box-sizing: border-box; margin: 0; padding: 0; }
  html, body {
    width: 1200px; height: 898px; overflow: hidden;
    background: var(--backdrop);
    font-family: "Arimo", Arial, sans-serif;
  }
  .letterhead {
    position: absolute; left: 296px; top: 19px;
    width: 608px; height: 860px;
    background: var(--paper);
    overflow: hidden;
    box-shadow: 0 10px 30px rgba(0,0,0,.45);
  }
  .header {
    position: absolute; left: 0; top: 0; width: 100%; height: 96px;
    background: var(--charcoal);
  }
  .header-sheen { position: absolute; left: 0; top: 96px; width: 100%; height: 60px; }
  .brand {
    position: absolute; left: 34px; top: 48px;
    display: flex; align-items: center; gap: 10px;
  }
  .brand-square { width: 30px; height: 30px; background: var(--amber); }
  .brand-name {
    color: var(--amber); font-weight: 700; font-size: 19px; letter-spacing: .5px;
    line-height: 1;
  }
  .company-details {
    position: absolute; right: 30px; top: 18px; text-align: right;
    font-size: 9px; line-height: 11px; color: var(--white); letter-spacing: .2px;
  }
  .company-details .accent { color: var(--amber); }
  .recipient {
    position: absolute; right: 30px; top: 104px; text-align: right;
    font-size: 9.5px; line-height: 12px; color: var(--ink);
  }
  .letter-body {
    position: absolute; left: 52px; top: 270px; width: 500px;
    font-size: 10.5px; line-height: 13px; color: var(--ink);
  }
  .letter-body p { margin-bottom: 17px; }
  .closing { margin-top: 8px; }
  .sender {
    position: absolute; left: 62px; top: 610px;
    font-size: 12px; line-height: 15px; color: var(--ink);
  }
  .sender .credential { font-size: 8px; letter-spacing: .3px; }
  .signature {
    position: absolute; left: 68px; top: 690px; width: 120px; height: 48px;
    background: linear-gradient(90deg, rgba(120,120,120,0) 0%, rgba(120,120,120,.18) 50%, rgba(120,120,120,0) 100%);
    border-radius: 24px;
  }
  .footer-shape { position: absolute; left: 0; bottom: 0; width: 100%; height: 230px; }
  .footer-mark {
    position: absolute; left: 286px; top: 676px; width: 28px; height: 28px;
    background: var(--grey-mark);
  }
  .footer-contacts {
    position: absolute; left: 0; bottom: 34px; width: 100%; text-align: center;
    font-size: 8.5px; font-weight: 700; letter-spacing: .6px; color: var(--charcoal);
  }
</style>
</head>
<body>
  <article class="letterhead">
    <header class="header">
      <div class="brand">
        <span class="brand-square"></span>
        <span class="brand-name">TARVEL BUILDING GROUP</span>
      </div>
      <div class="company-details">
        <div class="accent">www.TARVELGROUP.COM.AU</div>
        <div>REGISTERED BUILDING PRACTITIONER</div>
        <div><span class="accent">ABN:</span> 47 318 264 105</div>
      </div>
    </header>
    <svg class="header-sheen" viewBox="0 0 608 60" preserveAspectRatio="none">
      <polygon points="0,0 608,0 608,8 0,40" fill="#ececec"/>
      <polygon points="0,40 608,8 608,14 0,50" fill="#e2e2e2"/>
    </svg>

    <address class="recipient" style="font-style:normal">
      Name of Recipient<br>Company Name<br>Address as required<br>City, Province<br>Country, Postal Code
    </address>

    <section class="letter-body">
      <p>Salutation:</p>
      <p>Lorem ipsum dolor sit amet, consectetur adipscing elit, sed diam nonumy eiusmod tempor incidunt ut labore et dolore magna aliquam erat volupat. Ut enim ad minimim veniami quis nostrud exercitation ullamcorpor suscipit laboris nisi ut aliquip ex ea commodo consequat. Duis autem vel eum irure dolor in reprehenderit in voluptate velit esse molestaie son consequat, vel illum dolore eu fugiat nulla pariatur.</p>
      <p>At vero eos et accusam et justo odio dignissim qui blandit praesent lupatum delenit aigue duos dolor et molestais exceptur sint occaecat cupidat non provident, simil tempor sunt in culpa qui officia deserunt mollit anim id est dolor fugai. Et harum dereud facilis est er expedit distinct. Nam liber a tempor cum soluta nobis eligent optio comque nihil quod a impedit anim id quod maxim placeat facer possim omnis es voluptas assumenda est, omnis dolor repellend.</p>
      <p>Lorem ipsum dolor sit amet, consectetur adipscing elit, sed diam nonumy eiusmod tempor incidunt ut labore et dolore magna aliquam erat volupat. Ut enim ad minimim veniami quis nostrud exercitation ullamcorpor suscipit laboris nisi ut aliquip ex ea commodo consequat. Duis autem vel eum irure dolor in reprehenderit in voluptate velit esse molestaie son consequat, vel illum dolore.</p>
      <p class="closing">Complimentary closing</p>
    </section>

    <div class="sender">
      Sender’s Name, <span class="credential">CREDENTIAL</span><br>
      Title<br>
      Tel: 604-123-4567<br>
      Fax: 604-123-4567
    </div>
    <div class="signature" role="img" aria-label="Handwritten signature of the sender"></div>

    <svg class="footer-shape" viewBox="0 0 608 230" preserveAspectRatio="none">
      <path d="M0,150 Q300,110 608,20" fill="none" stroke="var(--amber)" stroke-width="3"/>
      <path d="M0,160 Q300,120 608,30 L608,230 L0,230 Z" fill="var(--amber)"/>
    </svg>
    <div class="footer-mark"></div>
    <footer class="footer-contacts">
      OFFICE PHONE: 03 58206317 | MOBILE NUMBER: 0413865290 | EMAIL: INFO@TARVELGROUP.COM.AU
    </footer>
  </article>
</body>
</html>
```